Australian Meat, Seafood and Fresh Produce Website

Our organization is looking to design a simple, but eye catching website to show our services.
Our company exports West Australian FRESH fruit and vegetables, seafood and meat.
The website we are looking for would consist of:
- Landing Page
- Company info
- Directors bio
- Page that highlights our products
- Contact us page
We would like it to have a Chinese translated version as well.
Tobin
Target Market(s)
Chinese Market
Industry/Entity Type
It Company
Number of Pages Required
1 page
Look and feel
Each slider illustrates characteristics of the customer's brand and the style your logo design should communicate.

```html
<!DOCTYPE html>
<html lang="en">
<head>
<meta charset="utf-8">
<title>Southport Harvest</title>
<link rel="stylesheet" href="https://fonts.googleapis.com/css2?family=Arimo:ital,wght@0,400;0,700;1,400&family=Gelasio:ital,wght@0,400;1,400&display=swap">
<style>
:root{
  --brown:#8d6e3b;
  --brown-dark:#7a5e30;
  --ink:#222;
  --text:#555;
  --muted:#777;
  --cream:#f4f0ea;
  --dark:#2f2f2f;
  --input:#333;
  --white:#fff;
}
*{margin:0;padding:0;box-sizing:border-box}
html,body{width:1200px;height:3219px;overflow:hidden;background:var(--white)}
body{font-family:"Arimo",Arial,sans-serif;color:var(--text);position:relative}
.abs{position:absolute}
.serif{font-family:"Gelasio",Georgia,serif}

/* header */
.site-header{position:absolute;left:0;top:0;width:1200px;height:132px}
.header-phone{left:184px;top:36px;font-size:13px;color:var(--ink)}
.header-phone b{font-weight:700}
.rule{position:absolute;height:1px;background:#bbb}
.rule::after{content:"";position:absolute;left:50%;top:-3px;width:6px;height:6px;background:var(--white);border:1px solid #999;transform:translateX(-50%) rotate(45deg)}
.brand{left:0;width:1200px;top:28px;text-align:center;font-size:27px;font-weight:700;color:var(--ink);letter-spacing:1px}
.social{display:flex;gap:16px}
.social span{width:18px;height:18px;border-radius:50%;background:var(--ink);display:block}
.main-nav{left:223px;top:95px;width:755px;display:flex;justify-content:space-between;font-size:12px;font-weight:700;color:var(--ink);letter-spacing:.5px}
.main-nav .active{color:var(--brown)}

/* hero */
.hero{left:0;top:132px;width:1200px;height:428px;background:radial-gradient(ellipse at 55% 40%,#d9b9a6 0%,#b88a72 22%,#5a3a2a 45%,#2a1a12 75%,#180f0a 100%)}
.slide-arrow{position:absolute;top:193px;width:36px;height:37px;background:var(--brown);display:flex;align-items:center;justify-content:center}
.slide-arrow.prev{left:0}.slide-arrow.next{right:0}

/* feature boxes */
.feature{position:absolute;top:594px;width:262px;height:234px;background:var(--brown);color:var(--white);text-align:center}
.feature svg{position:absolute;left:50%;top:28px;transform:translateX(-50%)}
.feature h3{position:absolute;top:86px;width:100%;font-size:19px;font-weight:400}
.feature p{position:absolute;top:120px;left:38px;right:38px;font-size:11px;line-height:17px}
.pill{display:inline-block;background:var(--white);color:var(--brown);font-size:10px;font-weight:700;border-radius:18px}
.feature .pill{position:absolute;top:182px;left:50%;transform:translateX(-50%);width:104px;height:32px;line-height:32px}

/* about */
.about{left:0;top:882px;width:1200px;height:414px;background:linear-gradient(100deg,#111 0%,#1c1c1c 40%,#3a3530 60%,#2a2622 75%,#121212 100%);color:var(--white);text-align:center}
.about h2{position:absolute;top:64px;width:100%;font-size:24px;font-weight:400;letter-spacing:2px}
.about p{position:absolute;top:138px;left:256px;width:688px;font-size:13px;line-height:21px}
.about .pill{position:absolute;top:301px;left:540px;width:120px;height:37px;line-height:37px;color:var(--ink);font-size:11px}

/* products */
.products-photo{left:0;top:1320px;width:585px;height:390px;background:radial-gradient(ellipse at 45% 50%,#e9a77a 0%,#8db04a 35%,#5c8d2e 55%,#ffffff 78%)}
.section-title{font-family:"Gelasio",Georgia,serif;font-size:23px;color:var(--brown);font-weight:400}
.product-name{font-family:"Gelasio",Georgia,serif;font-style:italic;font-size:17px;color:var(--brown)}
.product-sub{font-size:13px;color:var(--ink)}
.product-desc{font-size:10.5px;line-height:17px;color:var(--muted);width:420px}
.btn{display:inline-block;background:var(--brown);color:var(--white);font-size:11px;font-weight:700;text-align:center}
.products-btn{left:611px;top:1670px;width:162px;height:33px;line-height:33px;border-radius:18px}

/* news & areas */
.band{left:0;top:1742px;width:1200px;height:537px;background:var(--cream)}
.news-item{position:absolute;left:184px;width:336px;height:93px;border-bottom:1px solid #ccc}
.news-date{position:absolute;left:0;top:10px;width:44px;text-align:center;font-family:"Gelasio",Georgia,serif;color:var(--brown)}
.news-date b{display:block;font-size:34px;font-weight:400;line-height:34px}
.news-date span{font-size:15px;letter-spacing:1px}
.news-text{position:absolute;left:59px;top:10px;width:277px;font-size:10.5px;line-height:17px;color:var(--muted)}
.news-more{position:absolute;right:0;top:69px;font-size:11px;font-weight:700;color:var(--ink)}
.world-map{left:540px;top:1841px;width:478px;height:293px;background:var(--brown);border-radius:40% 30% 35% 45%/40% 45% 30% 35%;opacity:.92}
.areas-text{left:540px;top:2152px;width:480px;font-size:13px;line-height:19px;color:var(--ink)}
.location-btn{left:540px;top:2205px;width:134px;height:37px;line-height:37px;border-radius:3px;font-size:10px}

/* feedback */
.feedback-title{left:0;top:2314px;width:1200px;text-align:center;font-family:"Gelasio",Georgia,serif;font-size:16px;letter-spacing:3px;color:var(--brown)}
.feedback-intro{left:448px;top:2375px;width:304px;font-size:11.5px;line-height:18px;color:var(--ink)}
.label{position:absolute;left:0;width:1200px;text-align:center;font-family:"Gelasio",Georgia,serif;font-style:italic;font-size:11px;color:var(--brown)}
.field{position:absolute;left:448px;width:304px;height:31px;background:var(--input);color:#999;font-size:11px;line-height:31px;text-align:center}
.field i{position:absolute;right:12px;top:10px;width:11px;height:11px;border-radius:50%;border:2px solid var(--brown)}
.comment{position:absolute;left:366px;top:2729px;width:468px;height:115px;background:var(--input);color:#999;font-size:11px;padding:10px 12px}
.send{left:540px;top:2874px;width:119px;height:33px;line-height:33px;border-radius:18px;font-family:"Gelasio",Georgia,serif;font-weight:400;font-size:12px}
.sketch{background:linear-gradient(135deg,#eeeeee,#d8d8d8)}

/* footer */
.site-footer{left:0;top:3007px;width:1200px;height:212px;background:var(--dark);border-top:5px solid #555;color:#aaa}
.foot-brand{left:197px;top:52px;font-size:17px;font-weight:700;color:var(--white);letter-spacing:1px}
.foot-nav{left:420px;width:374px;text-align:center;font-size:11px;font-weight:700;letter-spacing:.5px;color:#bbb}
.foot-nav span{margin:0 10px}
.foot-nav .active{color:var(--brown)}
.foot-social{left:914px;top:50px}
.foot-social span{background:#bbb}
.foot-rule{left:528px;top:101px;width:202px;height:1px;background:var(--brown)}
.foot-small{font-family:"Gelasio",Georgia,serif;font-style:italic;font-size:10.5px;line-height:24px;color:#bbb}
.foot-link{color:var(--brown);text-decoration:underline}
.foot-phones{right:182px;top:130px;text-align:right;font-size:11px;line-height:20px;color:var(--white)}
</style>
</head>
<body>

<header class="site-header">
  <div class="abs header-phone">+8 (800) <b>555-01-92</b></div>
  <div class="rule" style="left:184px;top:69px;width:98px"></div>
  <div class="abs brand">SOUTHPORT HARVEST</div>
  <div class="abs social" style="left:914px;top:34px"><span></span><span></span><span></span></div>
  <div class="rule" style="left:918px;top:69px;width:98px"></div>
  <nav class="abs main-nav">
    <span class="active">HOME</span><span>ABOUT US</span><span>OUR PRODUCTS</span><span>REVIEWS</span><span>OUR SERVICE</span><span>FEED BACK</span><span>CONTACTS</span>
  </nav>
</header>

<section class="abs hero" role="img" aria-label="Close-up photograph of a seared salmon fillet with cracked pepper">
  <div class="slide-arrow prev"><svg width="10" height="14"><path d="M8 1 2 7l6 6" fill="none" stroke="#fff" stroke-width="2"/></svg></div>
  <div class="slide-arrow next"><svg width="10" height="14"><path d="M2 1l6 6-6 6" fill="none" stroke="#fff" stroke-width="2"/></svg></div>
</section>

<section class="features">
  <article class="feature" style="left:184px">
    <svg width="36" height="44" viewBox="0 0 36 44"><path d="M9 3h18v12a9 9 0 0 1-18 0z M9 6H3v4a6 6 0 0 0 6 6 M27 6h6v4a6 6 0 0 1-6 6 M18 24v8 M11 40h14v-4H11z" fill="none" stroke="#fff" stroke-width="2.5"/></svg>
    <h3 class="serif">Sucess Story</h3>
    <p>Lorem ipsum dolor sit amet, consectetur adipiscing elit, sed do eiusmod tempor incididunt aliqua</p>
    <span class="pill">READ MORE</span>
  </article>
  <article class="feature" style="left:468px">
    <svg width="52" height="40" viewBox="0 0 52 40"><circle cx="26" cy="22" r="13" fill="#fff"/><path d="M5 4v10M2 4v8a3 3 0 0 0 6 0V4M5 14v22M46 4c-4 3-4 12 0 14v18" fill="none" stroke="#fff" stroke-width="2.5"/></svg>
    <h3 class="serif">Our Services</h3>
    <p>Lorem ipsum dolor sit amet, consectetur adipiscing elit, sed do eiusmod tempor incididunt aliqua</p>
    <span class="pill">READ MORE</span>
  </article>
  <article class="feature" style="left:754px">
    <svg width="30" height="44" viewBox="0 0 30 44"><path d="M15 42C6 28 2 21 2 14a13 13 0 0 1 26 0c0 7-4 14-13 28z" fill="none" stroke="#fff" stroke-width="2.5"/><circle cx="15" cy="14" r="5" fill="#fff"/></svg>
    <h3 class="serif">Location</h3>
    <p>Lorem ipsum dolor sit amet, consectetur adipiscing elit, sed do eiusmod tempor incididunt aliqua</p>
    <span class="pill">READ MORE</span>
  </article>
</section>

<section class="abs about" aria-labelledby="about-title">
  <div class="abs" style="inset:0" role="img" aria-label="Dark photograph of a plated seafood dish"></div>
  <h2 id="about-title" class="serif">ABOUT US</h2>
  <div class="rule" style="left:554px;top:111px;width:92px;background:#ccc"></div>
  <p>Southport Harvest (SPH) aims to supply high quality West Australian produce to the rest of the World. Western Australia is known for its high quality farming practices and environment, which produces meat, seafood, fruit and vegetable of a caliber that is respected globally.<br>With a management team and first class suppliers allows our organization to provide quality ingredients, straight from farm or ocean to purchaser, in a timely manner to the highest quality.<br>This document aims to outline both our management team and their back grounds, as well as the suppliers who will initially be supply our global customers.</p>
  <span class="pill">LEARN MORE</span>
</section>

<section class="products">
  <div class="abs products-photo" role="img" aria-label="Photograph of a prawn and olive salad on a white plate"></div>
  <h2 class="abs section-title" style="left:611px;top:1332px">Export Products List</h2>
  <div class="rule" style="left:611px;top:1378px;width:104px"></div>
  <h3 class="abs product-name" style="left:611px;top:1405px">Seafood</h3>
  <div class="abs product-sub" style="left:611px;top:1434px">Grain Fed (min 150 days)</div>
  <p class="abs product-desc" style="left:611px;top:1458px">150-day fed catch graded by size scores 1, 2, 3 that ensures you will have a grade of high-quality stock to suit every sector of the market. Extremely well handled from all grounds combined with a careful chilling process that delivers every time.</p>
  <h3 class="abs product-name" style="left:611px;top:1528px">Meat</h3>
  <div class="abs product-sub" style="left:611px;top:1557px">Grain Fed (min 150 days)</div>
  <p class="abs product-desc" style="left:611px;top:1581px">150-day mid fed cattle high quality Angus beef. Available in various marble scores this beef will simply deliver in all the areas that matter: texture, marbling, flavor and consistency. No doubt the best quality you can serve in markets where it matters. Medium to long fed Angus bred cattle, it does not get any better. The choice of all the leading</p>
  <span class="abs btn products-btn">VIEW MORE PRODUCTS</span>
</section>

<section class="abs band"></section>
<h2 class="abs section-title" style="left:184px;top:1781px">Letest news &amp; events</h2>
<div class="rule" style="left:184px;top:1824px;width:104px;background:#bbb"></div>
<div class="news-item" style="top:1852px"><div class="news-date"><b>01</b><span>JAN</span></div><p class="news-text">Lorem Ipsum is that it has a more-or-less normal distribution of letters, as opposed to using 'Content here, content here', making it look like readable English.</p><span class="news-more">View More...</span></div>
<div class="news-item" style="top:1945px"><div class="news-date"><b>20</b><span>MAY</span></div><p class="news-text">Lorem Ipsum is that it has a more-or-less normal distribution of letters, as opposed to using 'Content here, content here', making it look like readable English.</p><span class="news-more">View More...</span></div>
<div class="news-item" style="top:2038px"><div class="news-date"><b>14</b><span>JULY</span></div><p class="news-text">Lorem Ipsum is that it has a more-or-less normal distribution of letters, as opposed to using 'Content here, content here', making it look like readable English.</p><span class="news-more">View More...</span></div>
<div class="news-item" style="top:2131px"><div class="news-date"><b>30</b><span>DEC</span></div><p class="news-text">Lorem Ipsum is that it has a more-or-less normal distribution of letters, as opposed to using 'Content here, content here', making it look like readable English.</p><span class="news-more">View More...</span></div>

<h2 class="abs section-title" style="left:540px;top:1781px">Production areas</h2>
<div class="rule" style="left:540px;top:1824px;width:104px;background:#bbb"></div>
<div class="abs world-map" role="img" aria-label="World map showing production and export regions"></div>
<p class="abs areas-text">Lorem ipsum dolor sit amet, consectetur adipiscing elit Lorem ipsum dolor sit amet, consectetur adipiscing elit Lorem ipsum dolor sit amet, consectetur</p>
<span class="abs btn location-btn">LOCATION DETAILS &#8250;</span>

<section class="feedback">
  <h2 class="abs feedback-title">FEED BACK</h2>
  <div class="rule" style="left:554px;top:2348px;width:92px"></div>
  <div class="abs sketch" style="left:184px;top:2361px;width:184px;height:115px" role="img" aria-label="Pencil sketch of a pizza"></div>
  <p class="abs feedback-intro">Lorem Ipsum is simply dummy text of the printing and typesetting industry. Lorem Ipsum has been the industry's standard dummy text ever since the 1500s</p>
  <label class="label" style="top:2474px">Your name:</label>
  <div class="field" style="top:2495px">Jared Tobin<i></i></div>
  <label class="label" style="top:2552px">E-mail:</label>
  <div class="field" style="top:2573px"><i></i></div>
  <label class="label" style="top:2630px">Phone number:</label>
  <div class="field" style="top:2651px">+8 800 555 01 67</div>
  <label class="label" style="top:2708px">Comment:</label>
  <div class="comment">Hi my name is...</div>
  <span class="abs btn send">Send message</span>
  <div class="abs sketch" style="left:840px;top:2838px;width:178px;height:162px" role="img" aria-label="Pencil sketch of a leg of ham"></div>
</section>

<footer class="abs site-footer">
  <div class="abs foot-brand">SOUTHPORT HARVEST</div>
  <div class="abs foot-nav" style="top:48px"><span class="active">HOME</span><span>ABOUT US</span><span>OUR PRODUCT</span><span>REVIEWS</span></div>
  <div class="abs foot-nav" style="top:72px"><span>OUR SERVICE</span><span>FEED BACK</span><span>CONTACTS</span></div>
  <div class="abs social foot-social"><span></span><span></span><span></span></div>
  <div class="abs foot-rule"></div>
  <div class="abs foot-small" style="left:227px;top:128px">© southportharvest 2015<br>NY 103</div>
  <div class="abs foot-small" style="left:444px;top:152px">&#9679; <span class="foot-link">Show on map</span></div>
  <div class="abs foot-small" style="left:609px;top:152px">&#10148; <span class="foot-link">hello@southportharvest.example</span></div>
  <div class="abs foot-phones">+8 800 555 01 67<br>+8 800 555 02 21</div>
</footer>

</body>
</html>
```